Hadley & Partners, LLC Business Card 2016

We need a new business card design for a very important trade show coming up.

We are a compliance Consulting Firm. Our clients are stock brokerage firms and investment advisers.

I would like our logo on both sides of the card.

Info in the front of the card shold include:

Logo
First & Last Name
Title
Office #
Cell #
Email
Company Address (42 W. Calloway St., Suite 300 Pasadena, CA 91417

Back of the card should include the logo and url: www.hadleypartnersgroup.com

Target Market(s)

Stock Brokerage Firms and Investment Advisers

Industry/Entity Type

Financial Service

Contact Information for Business Card

Marcus J. Pellew
President
42 W. Calloway St., Suite 300
Pasadena, CA 91417
O 626.555.0147 ext. 204
C 818.555.0193
Email: marcus@hadleypartnersgroup.com
www.hadleypartnersgroup.com

Requirements
Nice to have
• The back of the card could be black with the logo with the white letters.
• I do want the front of the card to at least have the color logo with the black "Hadley & Partners Lettering.

```html
<!DOCTYPE html>
<html lang="en">
<head>
<meta charset="utf-8">
<title>Hadley &amp; Partners — Business Card</title>
<link href="https://fonts.googleapis.com/css2?family=Montserrat:wght@400;600&display=swap" rel="stylesheet">
<style>
  :root {
    --backdrop: #dcdcdc;
    --paper: #f1f1f1;
    --ink: #111111;
    --black: #060606;
    --red: #c41217;
    --white: #ffffff;
    --muted: #3a3a3a;
  }
  * { box-sizing: border-box; margin: 0; padding: 0; }
  html, body { width: 1200px; height: 899px; overflow: hidden; }
  body {
    background: var(--backdrop);
    font-family: "Montserrat", sans-serif;
    position: relative;
  }
  .card {
    position: absolute;
    width: 600px;
    height: 343px;
    left: 300px;
    box-shadow: 0 6px 18px rgba(0,0,0,.18);
    overflow: hidden;
  }
  .card--back { top: 70px; background: var(--paper); }
  .card--front { top: 476px; display: flex; }

  .brand { display: flex; align-items: center; gap: 16px; }
  .brand__mark { width: 34px; height: 34px; background: var(--red); flex: none; }
  .brand__name { font-weight: 600; letter-spacing: .04em; white-space: nowrap; }

  .card--back .brand {
    position: absolute; left: 50%; top: 50%;
    transform: translate(-50%, -50%);
  }
  .card--back .brand__name { color: var(--ink); font-size: 34px; }

  .front__identity {
    width: 270px; background: var(--black);
    display: flex; align-items: center; justify-content: center;
  }
  .front__identity .brand { flex-direction: column; gap: 14px; }
  .front__identity .brand__mark { width: 40px; height: 40px; }
  .front__identity .brand__name { color: var(--white); font-size: 22px; }

  .front__band {
    width: 66px; background: var(--red);
    display: flex; flex-direction: column; align-items: center;
    padding-top: 100px; gap: 22px;
  }
  .front__band svg { width: 20px; height: 20px; fill: none; stroke: var(--white); stroke-width: 1.4; }

  .front__contact {
    flex: 1; background: var(--paper); color: var(--ink);
    padding: 38px 0 0 18px;
    font-size: 10.5px; line-height: 1.5;
  }
  .contact__name { font-weight: 600; font-size: 17px; line-height: 1.2; }
  .contact__title { font-size: 13px; color: var(--muted); margin-bottom: 12px; }
  .contact__group { margin-bottom: 12px; }
</style>
</head>
<body>

<section class="card card--back" aria-label="Card back">
  <div class="brand">
    <span class="brand__mark"></span>
    <span class="brand__name">Hadley &amp; Partners</span>
  </div>
</section>

<section class="card card--front" aria-label="Card front">
  <div class="front__identity">
    <div class="brand">
      <span class="brand__mark"></span>
      <span class="brand__name">Hadley &amp; Partners</span>
    </div>
  </div>

  <div class="front__band">
    <svg viewBox="0 0 20 20" aria-label="Phone"><rect x="6" y="2" width="8" height="16" rx="1.5"/><line x1="9" y1="15.5" x2="11" y2="15.5"/></svg>
    <svg viewBox="0 0 20 20" aria-label="Email"><rect x="2" y="5" width="16" height="11"/><polyline points="2,5 10,11 18,5"/></svg>
    <svg viewBox="0 0 20 20" aria-label="Website"><rect x="2" y="3" width="16" height="11"/><line x1="10" y1="14" x2="10" y2="17"/><line x1="6" y1="17" x2="14" y2="17"/></svg>
    <svg viewBox="0 0 20 20" aria-label="Address"><path d="M10 18s-5.5-6-5.5-9.5a5.5 5.5 0 0 1 11 0C15.5 12 10 18 10 18z"/><circle cx="10" cy="8.5" r="2"/></svg>
  </div>

  <div class="front__contact">
    <p class="contact__name">Marcus J. Pellew</p>
    <p class="contact__title">President</p>
    <div class="contact__group">
      <p>O 626.555.0147 ext. 204</p>
      <p>C 818.555.0193</p>
    </div>
    <p class="contact__group">marcus@hadleypartnersgroup.com</p>
    <p class="contact__group">www.hadleypartnersgroup.com</p>
    <div class="contact__group">
      <p>42 W. Calloway St., Suite 300</p>
      <p>Pasadena, CA 91417</p>
    </div>
  </div>
</section>

</body>
</html>
```